Business card, postcard, pocket folder

We are a real estate team and have had a new logo designed. From this, we need the following deliverables:- Business Cards (double-sided)- Just Listed / Just Sold Postcards (double-sided)- Pocket Folder. See logo attached.More work possible for the winning designer.
There are 5 members of the team, so head shots should be easily changed and possible for a group photo might be a good idea for the pocket folder but not 100% neccessary.
Target Market(s)
Real estate
Industry/Entity Type
Real Estate
Font styles to use
Serif
Sans Serif
Requirements
Must have
- Business cards and postcards must have a head shot on them.

```html
<!DOCTYPE html>
<html lang="en">
<head>
<meta charset="utf-8">
<title>Halvercroft Group – Stationery Set</title>
<link href="https://fonts.googleapis.com/css2?family=Questrial&display=swap" rel="stylesheet">
<style>
:root{
  --navy:#25408f;
  --red:#d71f2b;
  --white:#ffffff;
  --stage:#1c1c1c;
  --ink:#25408f;
}
*{box-sizing:border-box;margin:0;padding:0}
html,body{width:1189px;height:1200px;overflow:hidden;background:var(--stage)}
body{position:relative;font-family:"Questrial",sans-serif;color:var(--ink)}
.abs{position:absolute}
.brand{display:flex;align-items:center;gap:6px;font-family:"Questrial",sans-serif;white-space:nowrap}
.brand .mark{display:block;background:var(--red)}
.brand .name{color:var(--navy)}
.brand.on-dark .name{color:var(--white)}
.photo{background:linear-gradient(160deg,#7a8a9c,#3b3f48 60%,#1e2024)}
.headshot{background:linear-gradient(180deg,#9fb08a,#c9a98a 45%,#2c2f3a 80%)}
.row{display:flex;align-items:center;gap:6px}
.icon{flex:none}
.tiny{font-size:7px;line-height:1.25;color:var(--white)}
.social{display:flex;gap:6px}
.social span{display:block;background:var(--white)}

/* folder */
.folder{left:59px;top:38px;width:879px;height:784px}
.folder-top{left:0;top:0;width:879px;height:223px;background:var(--white)}
.folder-rule-red{left:0;top:223px;width:879px;height:7px;background:var(--red)}
.folder-photo{left:0;top:237px;width:879px;height:237px}
.folder-info{left:0;top:478px;width:879px;height:76px;background:var(--navy)}
.folder-web{left:0;top:558px;width:879px;height:24px;background:var(--red)}
.folder-flaps{left:0;top:586px;width:879px;height:198px}
.tagline{font-style:italic;color:var(--white);text-align:center;font-size:12px;line-height:1.35}
.web{color:var(--white);letter-spacing:3px;font-size:8px;white-space:nowrap}
.web-band-narrow{left:0;width:100%;text-align:center;letter-spacing:1.6px}

/* business card */
.card{border-radius:8px;overflow:hidden}
</style>
</head>
<body>

<!-- Pocket folder -->
<section class="abs folder">
  <div class="abs folder-top">
    <div class="abs brand" style="left:600px;top:100px">
      <span class="mark" style="width:14px;height:14px"></span>
      <span class="name" style="font-size:24px">Halvercroft Group</span>
    </div>
  </div>
  <div class="abs folder-rule-red"></div>
  <div class="abs folder-photo photo" role="img" aria-label="Group photo of the team"></div>
  <div class="abs folder-info">
    <div class="abs row" style="left:30px;top:28px">
      <svg class="icon" width="16" height="16" viewBox="0 0 16 16"><circle cx="8" cy="8" r="7" fill="#fff"/><path d="M5 4l2 0 1 2-1 1c.5 1 1.5 2 2.5 2.5l1-1 2 1v2c-4 0-7.5-3.5-7.5-7.5z" fill="#25408f"/></svg>
      <div class="tiny">Mobile: (555) 018-2746<br>Office: (555) 018-2746</div>
      <span style="width:1px;height:16px;background:#fff;margin:0 8px"></span>
      <svg class="icon" width="16" height="16" viewBox="0 0 16 16"><circle cx="8" cy="8" r="7" fill="#fff"/><circle cx="8" cy="8" r="4" fill="none" stroke="#25408f" stroke-width="1.4"/></svg>
      <div class="tiny">info@halvercroftmail.com<br>www.halvercroftgroup.com</div>
      <span style="width:1px;height:16px;background:#fff;margin:0 8px"></span>
      <svg class="icon" width="16" height="16" viewBox="0 0 16 16"><circle cx="8" cy="8" r="7" fill="#fff"/><path d="M8 3.5a3 3 0 0 1 3 3c0 2.3-3 5.5-3 5.5S5 8.8 5 6.5a3 3 0 0 1 3-3z" fill="#25408f"/></svg>
      <div class="tiny">PO Box 48, Kestrel Road<br>7 Larkin Street, Fitzroy, Australia</div>
    </div>
    <p class="abs tagline" style="left:570px;top:14px;width:300px">Lorem Ipsum is simply dummy text<br>of the<br>printing and typesetting industry..</p>
  </div>
  <div class="abs folder-web">
    <div class="abs social" style="left:186px;top:6px"><span style="width:12px;height:12px"></span><span style="width:12px;height:12px"></span><span style="width:12px;height:12px"></span></div>
    <div class="abs web" style="left:570px;top:8px">www.HALVERCROFTGROUP.com</div>
  </div>
  <svg class="abs folder-flaps" width="879" height="198" viewBox="0 0 879 198">
    <polygon points="0,0 437,0 416,198 0,198" fill="#25408f"/>
    <polygon points="443,0 879,0 877,198 462,198" fill="#25408f"/>
    <g stroke="#fff" stroke-width="1.5">
      <line x1="102" y1="35" x2="130" y2="7"/><line x1="287" y1="7" x2="315" y2="35"/>
      <line x1="102" y1="148" x2="130" y2="176"/><line x1="287" y1="176" x2="315" y2="148"/>
    </g>
  </svg>
  <div class="abs brand on-dark" style="left:135px;top:680px;transform:rotate(180deg)">
    <span class="name" style="font-size:22px">Halvercroft Group</span>
  </div>
</section>

<!-- Postcard front -->
<section class="abs" style="left:60px;top:887px;width:379px;height:268px;background:var(--white)">
  <div class="abs brand" style="left:28px;top:60px">
    <span class="mark" style="width:10px;height:10px"></span>
    <span class="name" style="font-size:17px">Halvercroft Group</span>
  </div>
  <div class="abs" style="left:0;top:114px;width:379px;height:38px;background:var(--navy)">
    <div class="abs row" style="left:28px;top:11px">
      <svg class="icon" width="16" height="16" viewBox="0 0 16 16"><circle cx="8" cy="8" r="7" fill="none" stroke="#fff" stroke-width="1.4"/><path d="M5.5 4.5l1.5 0 .8 1.6-.8.8c.5.9 1.2 1.6 2 2l.8-.8 1.6.8v1.5c-3.2 0-5.9-2.7-5.9-5.9z" fill="#fff"/></svg>
      <div class="tiny" style="font-size:8px">Mobile: (555) 018-2746<br>Office: (555) 018-2746</div>
    </div>
  </div>
  <div class="abs" style="left:0;top:152px;width:379px;height:38px;background:var(--red)">
    <div class="abs row" style="left:28px;top:11px">
      <svg class="icon" width="16" height="16" viewBox="0 0 16 16"><circle cx="8" cy="8" r="7" fill="none" stroke="#fff" stroke-width="1.4"/><path d="M8 4a2.6 2.6 0 0 1 2.6 2.6c0 2-2.6 4.8-2.6 4.8S5.4 8.6 5.4 6.6A2.6 2.6 0 0 1 8 4z" fill="#fff"/></svg>
      <div class="tiny" style="font-size:8px">PO Box 48, Kestrel Road<br>7 Larkin Street, Fitzroy, Australia</div>
    </div>
  </div>
  <div class="abs" style="left:226px;top:41px;width:114px;height:151px;background:#c8ccd6;padding:3px">
    <div class="headshot" role="img" aria-label="Head shot of the agent" style="width:100%;height:100%"></div>
    <div class="abs" style="left:3px;bottom:3px;width:108px;height:30px;background:rgba(37,64,143,.85);color:#fff;text-align:center;font-size:12px;line-height:1.05;padding-top:3px">Mara Ellison<br><span style="font-size:9px">President</span></div>
  </div>
  <p class="abs" style="left:29px;top:207px;width:322px;font-size:7px;line-height:1.35;text-align:justify;color:var(--navy)">Lorem Ipsum is simply dummy text of the printing and typesetting industry. Lorem Ipsum has been the industry's standard dummy text ever since the 1500s.</p>
  <div class="abs" style="left:0;top:239px;width:264px;height:16px;background:var(--red)">
    <div class="abs web" style="left:30px;top:4px">www.HALVERCROFTGROUP.com</div>
  </div>
  <div class="abs social" style="left:273px;top:239px"><span style="width:16px;height:16px;background:var(--navy)"></span><span style="width:16px;height:16px;background:var(--navy)"></span><span style="width:16px;height:16px;background:var(--red)"></span></div>
</section>

<!-- Postcard back -->
<section class="abs" style="left:465px;top:885px;width:381px;height:270px;background:var(--white)">
  <div class="abs" style="left:0;top:0;width:197px;height:229px;background:var(--navy)">
    <div class="abs brand on-dark" style="left:22px;top:66px">
      <span class="mark" style="width:10px;height:10px"></span>
      <span class="name" style="font-size:16px">Halvercroft Group</span>
    </div>
    <p class="abs tagline" style="left:0;top:124px;width:197px;font-size:8px">Lorem Ipsum is simply dummy text<br>of the<br>printing and typesetting industry..</p>
    <div class="abs" style="left:0;top:206px;width:197px;height:23px;background:var(--red)">
      <div class="abs web web-band-narrow" style="top:7px">www.HALVERCROFTGROUP.com</div>
    </div>
  </div>
</section>

<!-- Business card front -->
<section class="abs card" style="left:871px;top:845px;width:262px;height:148px;background:var(--navy)">
  <div class="abs brand on-dark" style="left:58px;top:64px">
    <span class="mark" style="width:9px;height:9px"></span>
    <span class="name" style="font-size:15px">Halvercroft Group</span>
  </div>
</section>

<!-- Business card back -->
<section class="abs card" style="left:871px;top:1006px;width:262px;height:149px;background:var(--white)">
  <div class="abs brand" style="left:14px;top:44px">
    <span class="mark" style="width:8px;height:8px"></span>
    <span class="name" style="font-size:13px">Halvercroft Group</span>
  </div>
  <div class="abs" style="left:0;top:80px;width:262px;height:12px;background:var(--red)">
    <div class="abs" style="left:16px;top:1px;font-size:8px;color:#fff;white-space:nowrap">Mara Ellison | <span style="font-size:6px">President</span></div>
  </div>
  <div class="abs" style="left:0;top:92px;width:262px;height:57px;background:var(--navy)">
    <div class="abs row" style="left:16px;top:5px;gap:5px">
      <svg class="icon" width="12" height="12" viewBox="0 0 16 16"><circle cx="8" cy="8" r="7" fill="#fff"/><path d="M5 4l2 0 1 2-1 1c.5 1 1.5 2 2.5 2.5l1-1 2 1v2c-4 0-7.5-3.5-7.5-7.5z" fill="#25408f"/></svg>
      <div class="tiny" style="font-size:6px">Mobile: (555) 018-2746<br>Office: (555) 018-2746</div>
    </div>
    <div class="abs" style="left:33px;top:23px;width:85px;height:1px;background:#fff"></div>
    <div class="abs row" style="left:16px;top:27px;gap:5px">
      <svg class="icon" width="12" height="12" viewBox="0 0 16 16"><circle cx="8" cy="8" r="7" fill="#fff"/><circle cx="8" cy="8" r="4" fill="none" stroke="#25408f" stroke-width="1.4"/></svg>
      <div class="tiny" style="font-size:6px">info@halvercroftmail.com<br>www.halvercroftgroup.com</div>
    </div>
    <div class="abs tiny" style="left:149px;top:28px;font-size:6px">PO Box 48, Kestrel Road<br>7 Larkin St, Fitzroy, Australia</div>
  </div>
  <div class="abs" style="left:178px;top:18px;width:66px;height:90px;background:#c8ccd6;padding:2px">
    <div class="headshot" role="img" aria-label="Head shot of the agent" style="width:100%;height:100%"></div>
    <div class="abs social" style="right:6px;bottom:6px;gap:3px"><span style="width:9px;height:9px;background:var(--red)"></span><span style="width:9px;height:9px;background:var(--red)"></span></div>
  </div>
</section>

</body>
</html>
```